Lantern Grove Bridal Show Flyer

I need designed a reusable flyer that is more eye catching than my current flyer. I would also need separate layers as the details change from show to show. I attached the flyer I currently use.

Wedding

```html
<!DOCTYPE html>
<html lang="en">
<head>
<meta charset="utf-8">
<title>Lantern Grove Bridal Show Flyer</title>
<link rel="stylesheet" href="https://fonts.googleapis.com/css2?family=Lato:wght@300;400;700;900&family=Great+Vibes&display=swap">
<style>
  :root {
    --plum: #7d2a7c;
    --plum-deep: #6a1f69;
    --orchid: #a04f9f;
    --lavender: #d9b3d8;
    --grey-text: #7a7a7a;
    --paper-top: #ffffff;
    --paper-bottom: #e9e9eb;
    --footer: #000000;
    --white: #ffffff;
  }
  * { margin: 0; padding: 0; box-sizing: border-box; }
  html, body { width: 927px; height: 1200px; overflow: hidden; background: var(--white); }
  .flyer {
    position: relative;
    width: 927px;
    height: 1200px;
    overflow: hidden;
    background: linear-gradient(180deg, var(--paper-top) 55%, var(--paper-bottom) 92%);
    font-family: "Lato", sans-serif;
  }
  .hero-photo {
    position: absolute;
    left: 0; top: 0;
    width: 927px; height: 620px;
    background:
      radial-gradient(ellipse at 30% 25%, #f6e3c2 0%, rgba(246,227,194,0) 45%),
      linear-gradient(90deg, #2c2623 0%, #5a4a3a 18%, #b59c78 35%, #d9c6a6 48%, #eeeae6 60%, #f4f2f0 100%);
  }
  .swoosh { position: absolute; left: 0; top: 0; width: 927px; height: 620px; }
  .show-title {
    position: absolute;
    right: 30px; top: 455px;
    font-family: "Great Vibes", cursive;
    font-size: 66px;
    color: var(--white);
    text-shadow: 2px 3px 4px rgba(60, 10, 60, 0.55);
  }
  .headline {
    position: absolute; left: 0; top: 625px; width: 927px;
    text-align: center;
    font-weight: 900;
    font-size: 60px;
    color: var(--plum);
    letter-spacing: 0.5px;
  }
  .subhead {
    position: absolute; left: 0; top: 692px; width: 927px;
    text-align: center;
    font-weight: 300;
    font-size: 47px;
    color: #222;
  }
  .prize-box {
    position: absolute;
    left: 208px; top: 770px;
    width: 506px; height: 112px;
    background: linear-gradient(180deg, #c69bc5 0%, var(--orchid) 45%, var(--plum-deep) 100%);
    box-shadow: 0 6px 10px rgba(0,0,0,0.25);
    color: var(--white);
    text-align: center;
  }
  .prize-note { font-size: 16px; font-weight: 400; line-height: 1; }
  .prize-note.top { padding-top: 8px; }
  .prize-amount { font-size: 60px; font-weight: 900; line-height: 1; margin: 2px 0 1px; text-shadow: 1px 2px 3px rgba(0,0,0,0.3); }
  .venue {
    position: absolute; left: 0; top: 906px; width: 927px;
    text-align: center; color: var(--plum);
  }
  .venue-name { font-size: 33px; font-weight: 700; line-height: 44px; }
  .venue-street { font-size: 29px; font-weight: 400; line-height: 36px; }
  .venue-city { font-size: 29px; font-weight: 400; line-height: 36px; color: var(--grey-text); }
  .coupon { font-size: 30px; font-weight: 700; line-height: 46px; }
  .footer {
    position: absolute; left: 0; top: 1104px;
    width: 927px; height: 96px;
    background: var(--footer);
    color: var(--white);
  }
  .ticket-info {
    position: absolute; left: 52px; top: 13px;
    font-family: "Lato", sans-serif;
    font-weight: 700;
    font-size: 19px;
    line-height: 25px;
  }
  .brand {
    position: absolute; right: 40px; top: 26px;
    display: flex; align-items: center; gap: 14px;
    font-weight: 400;
    font-size: 42px;
    line-height: 1;
    color: var(--white);
  }
  .brand-dot { width: 34px; height: 34px; border: 2px solid var(--white); border-radius: 50%; }
</style>
</head>
<body>
<main class="flyer">
  <div class="hero-photo" role="img" aria-label="Photograph of a bride and groom holding hands in warm backlit sunlight"></div>

  <svg class="swoosh" viewBox="0 0 927 620" aria-hidden="true">
    <defs>
      <linearGradient id="bandFill" x1="0" y1="0" x2="1" y2="0">
        <stop offset="0" stop-color="#8a3489"/>
        <stop offset="0.5" stop-color="#9b469a"/>
        <stop offset="1" stop-color="#7d2a7c"/>
      </linearGradient>
      <linearGradient id="ribbonFill" x1="0" y1="0" x2="1" y2="0">
        <stop offset="0" stop-color="#b27bb1"/>
        <stop offset="0.5" stop-color="#f1e2f0"/>
        <stop offset="1" stop-color="#c89ac7"/>
      </linearGradient>
    </defs>
    <path d="M0 500 C 180 460, 330 430, 520 428 C 700 426, 820 430, 927 445 L927 620 L0 620 Z" fill="url(#bandFill)"/>
    <path d="M0 560 C 180 520, 380 505, 560 540 C 700 565, 820 575, 927 560 L927 620 L0 620 Z" fill="url(#ribbonFill)"/>
    <path d="M0 585 C 200 548, 400 540, 580 565 C 720 585, 830 590, 927 578 L927 620 L0 620 Z" fill="#ffffff"/>
  </svg>

  <div class="show-title">Bridal Show</div>

  <h1 class="headline">OPEN CASTING CALL</h1>
  <h2 class="subhead">FIND YOUR DREAM DRESS</h2>

  <section class="prize-box">
    <p class="prize-note top">Lorem ipsum dolor sit amet, consectetur adipiscing</p>
    <p class="prize-amount">$25.000</p>
    <p class="prize-note">Mauris nulla ante, condimentum nec</p>
  </section>

  <section class="venue">
    <p class="venue-name">Pellentesque quis faucibus mi. Aenean</p>
    <p class="venue-street">1190 Willow Lane</p>
    <p class="venue-city">Fairhaven, CT</p>
    <p class="coupon">$ 3 off admission by using coupon code NP3</p>
  </section>

  <footer class="footer">
    <div class="ticket-info">
      <p>GET TICKETS AT</p>
      <p>LANTERNGROVE-EVENTS.COM</p>
      <p>555-014-2290</p>
    </div>
    <div class="brand">
      <span>Lantern Grove</span>
      <span class="brand-dot"></span>
    </div>
  </footer>
</main>
</body>
</html>
```